Velmar Intergrated Marketing Stationary Design Contest

We require a very professional looking stationary set to include: letterhead, compliments slip and business cards (double sided bus cards).

Files should be supplied on either Illustrator or InDesign.

We are interested in perhaps encorporating a faint watermark with the letter q or the logo, but it isnt a pre-requisite

Target Market(s)

Business owners seeking professional marketing services

Industry/Entity Type

Marketing

Requirements
Must have
• Concurrent theme wiht business cards, letterhead and comp slip. Must be an editable document for future ammendment
Should not have
• No use of times new roman or similar fonts

```html
<!DOCTYPE html>
<html lang="en">
<head>
<meta charset="utf-8">
<title>Velmar Intergrated Marketing – Stationery Set</title>
<link href="https://fonts.googleapis.com/css2?family=Carlito:wght@400;700&family=Pinyon+Script&display=swap" rel="stylesheet">
<style>
  :root{
    --bg:#fd7f7b;
    --sheet:#fd7f7b;
    --edge:#e2676a;
    --teal:#147a78;
    --purple:#7b4fd0;
  }
  html,body{margin:0;padding:0;width:1200px;height:857px;overflow:hidden;background:var(--bg);}
  body{font-family:"Carlito",sans-serif;color:var(--teal);position:relative;}
  .sheet{position:absolute;background:var(--sheet);border:1px solid var(--edge);box-sizing:border-box;}
  .brand{display:flex;align-items:center;gap:6px;color:var(--teal);font-weight:400;line-height:1;white-space:nowrap;}
  .brand-dot{border-radius:50%;background:var(--purple);flex:none;}
  .label{color:var(--purple);}

  /* business card front */
  .card-front{left:294px;top:63px;width:135px;height:241px;text-align:center;font-size:8.4px;line-height:11.6px;}
  .card-front .brand{position:absolute;left:9px;top:14px;font-size:19px;}
  .card-front .brand-dot{width:28px;height:28px;}
  .card-name{position:absolute;left:0;right:0;top:68px;color:var(--purple);font-size:10.5px;line-height:12px;}
  .card-role{position:absolute;left:0;right:0;top:81px;font-size:5.2px;letter-spacing:.2px;line-height:6px;}
  .card-contact{position:absolute;left:0;right:0;top:104px;}
  .card-address{position:absolute;left:0;right:0;top:164px;}

  /* business card back */
  .card-back{left:453px;top:63px;width:135px;height:241px;}
  .card-back .brand{position:absolute;left:11px;top:86px;font-size:19px;}
  .card-back .brand-dot{width:28px;height:28px;}

  /* compliments slip */
  .slip{left:72px;top:330px;width:514px;height:232px;}
  .slip .brand{position:absolute;left:22px;top:18px;font-size:34px;}
  .slip .brand-dot{width:46px;height:46px;}
  .slip-greeting{position:absolute;left:222px;top:12px;font-family:"Pinyon Script",cursive;color:var(--purple);font-size:40px;line-height:56px;white-space:nowrap;}
  .footer-lines{position:absolute;left:0;right:0;text-align:center;font-size:8.7px;line-height:14px;white-space:nowrap;}
  .slip .footer-lines{top:197px;}

  /* letterhead */
  .letterhead{left:606px;top:64px;width:513px;height:725px;}
  .letterhead .brand{position:absolute;left:158px;top:28px;font-size:38px;}
  .letterhead .brand-dot{width:52px;height:52px;}
  .letterhead .footer-lines{top:94px;}
  .legal{position:absolute;left:0;right:0;top:687px;text-align:center;font-size:8.7px;white-space:nowrap;word-spacing:1px;}
  .legal span{margin:0 8px;}
</style>
</head>
<body>

<section class="sheet card-front" aria-label="Business card front">
  <div class="brand"><span class="brand-dot"></span>Velmar</div>
  <div class="card-name">Ellis Harrow</div>
  <div class="card-role">GENERAL MANAGER</div>
  <div class="card-contact">
    www.velmarim.co.uk<br>
    ellis@velmarim.co.uk<br>
    <span class="label">T</span> 01632 960614<br>
    <span class="label">F</span> 01632 960611
  </div>
  <div class="card-address">
    Velmar Intergrated Marketing<br>
    Market Offices<br>
    Market Street<br>
    Holbeck<br>
    West Yorkshire<br>
    LS99 4QT
  </div>
</section>

<section class="sheet card-back" aria-label="Business card back">
  <div class="brand"><span class="brand-dot"></span>Velmar</div>
</section>

<section class="sheet slip" aria-label="Compliments slip">
  <div class="brand"><span class="brand-dot"></span>Velmar</div>
  <div class="slip-greeting">With Compliments</div>
  <div class="footer-lines">
    Velmar Intergrated Marketing | Market Office | Market Street | Holbeck | West Yorkshire | LS99 4QT<br>
    <span class="label">T</span> 01632 960614 | <span class="label">F</span> 01632 960611 | <span class="label">W</span> www.velmarim.co.uk | <span class="label">E</span> hello@velmarim.co.uk
  </div>
</section>

<section class="sheet letterhead" aria-label="Letterhead">
  <div class="brand"><span class="brand-dot"></span>Velmar</div>
  <div class="footer-lines">
    Velmar Intergrated Marketing | Market Office | Market Street | Holbeck | West Yorkshire | LS99 4QT<br>
    <span class="label">T</span> 01632 960614 | <span class="label">F</span> 01632 960611 | <span class="label">W</span> www.velmarim.co.uk | <span class="label">E</span> hello@velmarim.co.uk
  </div>
  <div class="legal"><span>Company registration 4817035</span><span>Vat No. 512 7731 40</span><span>Trading as a division of Brannock Ltd</span></div>
</section>

</body>
</html>
```